Landing page

I have a landing page script which has no design element whatsoever.
I need someone creative to take the script and make a design, including providing the HTML script once finished.
The landing page will include a video sales letter, some testimonials, 2 buttons (one which will show a pop-up with 3 confirmation checkboxes and another button which when pressed will open an embedded calendly window or pop-up.
Most importantly, the landing page must be designed with best conversion practises in mind.
The attached script is a draft, but the final copy it will be very similar in terms of length and content.
Branding package should be as per our website https://brightwarrowdispatch.com
e-Commerce store owners and dropshippers

```html
<!DOCTYPE html>
<html lang="en">
<head>
<meta charset="utf-8">
<title>Bright Warrow Dispatch – Find, import &amp; sell dropshippers product</title>
<link href="https://fonts.googleapis.com/css2?family=Roboto:wght@400;500;700&display=swap" rel="stylesheet">
<style>
:root{
  --red:#e8191f;
  --ink:#1f1f1f;
  --body:#333;
  --muted:#777;
  --band:#e1dfe0;
  --line:#dcdcdc;
  --white:#fff;
  --tint:#fbe3e4;
}
*{box-sizing:border-box;margin:0;padding:0}
html,body{width:1200px;height:4542px;overflow:hidden;background:var(--white)}
body{font-family:'Roboto',sans-serif;color:var(--body);position:relative}
.page{position:relative;width:1200px;height:4542px;overflow:hidden}
.abs{position:absolute}
.btn{position:absolute;display:flex;align-items:center;justify-content:center;background:var(--red);color:var(--white);font-size:11px;font-weight:500;text-decoration:none}
h1,h2,h3{color:var(--ink);font-weight:500}
.sec-title{position:absolute;left:0;width:1200px;text-align:center;font-size:28px;font-weight:500;color:var(--ink)}
.copy p{font-size:11px;line-height:1.65;color:var(--body);margin-bottom:17px}
.art{position:absolute;border-radius:6px}
.ring{position:absolute;border-radius:50%;border:2px dashed var(--red)}
.tint{position:absolute;background:var(--tint);opacity:.7}

/* nav */
.nav{position:absolute;top:0;left:0;width:1200px;height:64px;box-shadow:0 2px 8px rgba(0,0,0,.06)}
.logo{position:absolute;font-size:22px;font-weight:500;color:var(--red)}
.nav-links{position:absolute;left:481px;top:24px;display:flex;gap:26px;font-size:11px;font-weight:500;color:var(--ink)}
.login{position:absolute;left:930px;top:16px;width:67px;height:30px;border:1.5px solid var(--red);display:flex;align-items:center;justify-content:center;gap:5px;font-size:11px;font-weight:500;color:var(--ink)}

/* hero */
.hero-title{left:203px;top:128px;font-size:37px;line-height:1.12;font-weight:700}
.hero-title span{color:var(--red)}
.hero-sub{left:203px;top:263px;width:280px;font-size:11.5px;line-height:1.6}

/* featured */
.featured{position:absolute;top:540px;left:203px;width:794px;display:flex;justify-content:space-between;align-items:center}
.brand{display:flex;align-items:center;gap:8px;font-size:22px;font-weight:700;color:var(--ink)}
.brand i{display:block;width:22px;height:22px;background:var(--ink);border-radius:50%}
.brand .sq{border-radius:3px}

/* cards */
.card{position:absolute;top:722px;width:256px;height:423px;background:var(--white);box-shadow:0 2px 14px rgba(0,0,0,.12)}
.card h3{position:absolute;top:198px;left:0;width:100%;text-align:center;font-size:17px;line-height:1.3;font-weight:500}
.card ul{position:absolute;top:252px;left:22px;right:16px;list-style:none}
.card li{position:relative;padding-left:14px;font-size:10.5px;line-height:1.4;margin-bottom:9px;color:var(--body)}
.card li:before{content:"";position:absolute;left:0;top:4px;width:6px;height:6px;border-radius:50%;background:var(--red)}
.card .btn{left:22px;right:16px;bottom:17px;height:30px}

/* problems */
.problem{position:absolute;top:1700px;width:150px;text-align:center}
.problem .ring{left:28px;top:0;width:94px;height:94px}
.problem .icon{position:absolute;left:46px;top:18px;width:58px;height:58px;border-radius:50%}
.problem h4{position:absolute;top:108px;width:100%;font-size:14px;font-weight:500;color:var(--ink)}
.problem p{position:absolute;top:128px;left:15px;width:120px;font-size:10.5px;line-height:1.3}
.problem a{position:absolute;top:176px;width:100%;font-size:10.5px;font-weight:500;color:var(--ink);text-decoration:none}

.bullets{list-style:none;margin:-8px 0 14px}
.bullets li{position:relative;padding-left:13px;font-size:11px;line-height:1.9}
.bullets li:before{content:"";position:absolute;left:0;top:7px;width:6px;height:6px;border-radius:50%;background:var(--red)}

.center-copy p{text-align:center;font-size:11px;line-height:1.5;margin-bottom:15px}

/* footer */
.foot-col{position:absolute;top:4305px}
.foot-col h5{font-size:14px;font-weight:500;color:var(--ink);margin-bottom:15px}
.foot-col a{display:block;font-size:11px;color:var(--body);text-decoration:none;margin-bottom:15px}
</style>
</head>
<body>
<div class="page">

<!-- Navigation -->
<header class="nav">
  <div class="logo" style="left:203px;top:17px">LOGO</div>
  <nav class="nav-links"><span>Features</span><span>Pricing</span><span>Resources ▾</span><span>Blog</span></nav>
  <a class="btn" href="#" style="left:816px;top:16px;width:99px;height:30px">Get Started</a>
  <div class="login"><svg width="10" height="11" viewBox="0 0 10 11"><circle cx="5" cy="3" r="2.6" fill="#e8191f"/><path d="M0 11c0-3.5 2.2-5 5-5s5 1.5 5 5z" fill="#e8191f"/></svg>Login</div>
</header>

<!-- Hero -->
<h1 class="abs hero-title">Find , import &amp; sell<br><span>Dropshippers</span><br>product</h1>
<p class="abs hero-sub">Find the best Dropshipping suppliers from US, EU &amp; China and sell their products online.</p>
<a class="btn" href="#" style="left:203px;top:315px;width:128px;height:32px">Start your free trial</a>
<div class="art" role="img" aria-label="Store dashboard mock-up with product bubbles: handbag, leopard coat and watch with profit tags" style="left:617px;top:97px;width:382px;height:291px;background:linear-gradient(135deg,#f4f4f6,#e6e7eb 60%,#f7dcdc)"></div>

<!-- Featured on -->
<h2 class="sec-title" style="top:462px">Featured on</h2>
<div class="featured">
  <div class="brand" style="font-size:14px;font-weight:500"><i class="sq"></i>Cloudnest</div>
  <div class="brand">Leapcart</div>
  <div class="brand" style="font-size:15px;font-weight:500"><i></i>Launch Board</div>
  <div class="brand"><i class="sq"></i>Shopwell</div>
  <div class="brand">Sitecraft</div>
</div>

<!-- Our promise -->
<h2 class="sec-title" style="top:631px">Our promise</h2>
<div class="tint" role="img" aria-label="Red dotted decoration" style="left:132px;top:966px;width:225px;height:211px"></div>

<article class="card" style="left:203px">
  <div class="art" role="img" aria-label="Product catalogue screenshot with a straw hat in a circle" style="left:12px;top:18px;width:230px;height:168px;background:linear-gradient(135deg,#f2f2f4,#e3d9cc)"></div>
  <h3>Clearly auditing your<br>supply chain</h3>
  <ul><li>Sample products from multiple manufacturers</li><li>Shortlist based on quality and value</li><li>Negotiate pricing, reducing cost</li><li>Speeding up production &amp; processing time</li></ul>
  <a class="btn" href="#">Learn More</a>
</article>
<article class="card" style="left:472px">
  <div class="art" role="img" aria-label="Fashion store screenshot with headphones in a circle" style="left:12px;top:18px;width:230px;height:168px;background:linear-gradient(135deg,#f2f2f4,#d9dadd)"></div>
  <h3>Putting a smile on your<br>customer's face</h3>
  <ul><li>Options to brand, customise or improve your product</li><li>Review your product line and create a cost-effective packing solution</li><li>Improve your customer experience with proposed special inserts and gifts</li></ul>
  <a class="btn" href="#">Learn More</a>
</article>
<article class="card" style="left:742px">
  <div class="art" role="img" aria-label="Apparel grid screenshot with a backpack in a circle" style="left:12px;top:18px;width:230px;height:168px;background:linear-gradient(135deg,#f2f2f4,#e8d6cf)"></div>
  <h3>Finding hidden profits,<br>reducing shipping time</h3>
  <ul><li>Review your geographical sales and discuss opportunities</li><li>Advise and recommendation on utilising our worldwide 3PL network for next-day</li><li>Optimising your setup to fully automate the procurement and fulfilment process</li></ul>
  <a class="btn" href="#">Learn More</a>
</article>

<!-- How do I know this is real -->
<h2 class="abs" style="left:203px;top:1242px;font-size:27px">How do I know this is real?</h2>
<div class="abs copy" style="left:203px;top:1292px;width:410px">
  <p>Is this starting to sound too good to be true?</p>
  <p>Before you think this is a scam, I implore you to bookmark this page, or better yet, open a tab in your browser now.</p>
  <p>Copy and paste Bright Warrow Dispatch into Seekly search, hell, ask AskBot too if you're that well inclined.</p>
  <p>What you should find is 5* reviews on multiple platforms, a solid presence since early 2019, and no, genuinely negative feedback from anyone.</p>
</div>
<a class="btn" href="#" style="left:203px;top:1503px;width:127px;height:30px">Learn More</a>
<div class="art" role="img" aria-label="Smartwatch product photo above a five-star review card" style="left:714px;top:1221px;width:290px;height:338px;background:linear-gradient(160deg,#2a2a2e 0%,#3b3d44 40%,#f3f3f5 41%,#f3f3f5 100%)"></div>

<!-- What's holding me back -->
<h2 class="sec-title" style="top:1622px">What’s holding me back? (Reveal the REAL problem)</h2>
<div class="problem" style="left:260px">
  <div class="ring"></div><div class="icon" role="img" aria-label="Delivery truck icon" style="background:linear-gradient(135deg,#fde2e2,#f4a9a9)"></div>
  <h4>Fast shipping</h4><p>Imagine you have a great product-market fit, you can ride the wave, here</p><a href="#">Learn More...</a>
</div>
<div class="problem" style="left:432px">
  <div class="ring"></div><div class="icon" role="img" aria-label="Parcel box icon" style="background:linear-gradient(135deg,#fdebd8,#f0b98a)"></div>
  <h4>Fast processing</h4><p>Fast shipping and processing go hand in hand. When one fails, it</p><a href="#">Learn More...</a>
</div>
<div class="problem" style="left:600px">
  <div class="ring"></div><div class="icon" role="img" aria-label="Support agent icon" style="background:linear-gradient(135deg,#fde2e2,#f08a6c)"></div>
  <h4>Superior support</h4><p>It’s a great feeling to have someone you can rely on and trust. Getting back to</p><a href="#">Learn More...</a>
</div>
<div class="problem" style="left:771px">
  <div class="ring"></div><div class="icon" role="img" aria-label="Quality parcel with ribbon icon" style="background:linear-gradient(135deg,#fdf0d8,#f2c47e)"></div>
  <h4>Quality products</h4><p>You are serious about creating a brand and selling a product that</p><a href="#">Learn More...</a>
</div>

<!-- What is to blame -->
<div class="tint" role="img" aria-label="Red dotted decoration" style="left:138px;top:2090px;width:225px;height:236px"></div>
<div class="art" role="img" aria-label="Communication diagram: chat window surrounded by three team member portraits" style="left:190px;top:2000px;width:289px;height:300px;background:linear-gradient(135deg,#ffffff,#f0f0f2);border:3px solid var(--red)"></div>
<h2 class="abs" style="left:527px;top:1998px;font-size:27px">What is to blame?</h2>
<div class="abs copy" style="left:527px;top:2048px;width:410px">
  <p>Here’s the thing. Contrary to popular belief, your typical Chinese agent isn’t intentionally trying to wreck your business.</p>
  <p>In almost all cases, they actually do mean well.</p>
  <p>But practically, it just doesn’t work.</p>
  <p>I know first-hand how what may seem like a simple communication error literally leaves your e-Com store in ruins.</p>
</div>
<a class="btn" href="#" style="left:527px;top:2234px;width:127px;height:30px">Learn More</a>

<!-- Why now -->
<h2 class="abs" style="left:203px;top:2380px;font-size:27px">Why now?</h2>
<div class="abs copy" style="left:203px;top:2425px;width:410px">
  <p style="margin-bottom:14px">Let’s face it. You’re not in e-Commerce because you love it or are passionate about it (although those of you who are, have a big advantage!).<br>It’s because of the dream and destination you have engraved in your mind, right?<br>Let’s take it back to basics and ask some fundamental questions.<br>Would you answer yes or no to :</p>
  <ul class="bullets"><li>Do you enjoy your 9-5 or current lifestyle?</li><li>Are you happy with your job or career path?</li><li>Are you content working for others for the rest of your life?</li><li>Happy and look forward to waking up each work day?</li></ul>
</div>
<a class="btn" href="#" style="left:203px;top:2625px;width:128px;height:30px">Learn More</a>
<div class="art" role="img" aria-label="Accessories store screenshot with category panel and a travel bag shipping from the United States" style="left:629px;top:2372px;width:416px;height:324px;background:linear-gradient(135deg,#f5f5f6,#ebe6e2 55%,#f2d8d4)"></div>

<!-- Why should I trust you -->
<div class="abs" style="left:0;top:2757px;width:1200px;height:367px;background:var(--band)"></div>
<div class="tint" role="img" aria-label="Red dotted decoration" style="left:0;top:2757px;width:125px;height:150px;opacity:.5"></div>
<div class="tint" role="img" aria-label="Red dotted decoration" style="left:1065px;top:2975px;width:135px;height:149px;opacity:.5"></div>
<h2 class="sec-title" style="top:2810px">Why should I trust you?</h2>
<div class="abs center-copy" style="left:240px;top:2866px;width:720px">
  <p>And that’s where <b>WE</b> come in.</p>
  <p>Although, from here on out, I won’t be using WE, but rather I. Because it’s me, Rowan, personally writing this.<br>I didn’t hire a copywriter for any of this, or use AskBot. Neither did I seek advice and guidance for any of the copy.</p>
  <p>Whether you want to believe it or not, <b>I WANT</b> to change <b>YOUR</b> life for the better, that’s <b>MY</b> only concern.</p>
  <p>It’s not about money, business or status. For me, it’s about helping you achieve ultimate fulfilment (pun intended). I get way more pleasure<br>from helping others than any amount of money or power ever will.<br>In fact, I couldn’t care less about $s and material possessions. I could retire tomorrow if I wanted to (no, I’m not bragging).</p>
</div>
<a class="btn" href="#" style="left:536px;top:3038px;width:128px;height:29px">Learn More</a>

<!-- How can I get started -->
<div class="art" role="img" aria-label="Home decor store screenshot with pendant lamps, jacket, wristwatch and sneaker bubbles" style="left:150px;top:3189px;width:467px;height:370px;background:linear-gradient(135deg,#f6f6f7,#e9e9ec 55%,#dfe6f3)"></div>
<h2 class="abs" style="left:640px;top:3214px;font-size:27px">How can I get started?</h2>
<div class="abs copy" style="left:640px;top:3260px;width:400px">
  <p>All you have to do is complete the form below and I shall review your submission.<br>If there’s a high possibility that Bright Warrow Dispatch can help, and take you on, you’ll receive a URL to schedule a call with me.</p>
  <p>We can then discuss everything in detail to make sure we’re a good fit for each other.<br>If all is well, the onboarding process will begin, you’ll be invited to our dedicated Chatterly support, you’ll be assigned an account manager, and we’ll assist you in getting your store set up and streamlined.</p>
</div>
<a class="btn" href="#" style="left:640px;top:3469px;width:127px;height:30px">Learn More</a>

<!-- What do I have to lose -->
<h2 class="abs" style="left:203px;top:3621px;font-size:27px">What do I have to lose?</h2>
<div class="abs copy" style="left:203px;top:3671px;width:410px">
  <p>There is one big caveat, however, and that is LIMITED SLOTS!</p>
  <p>There is a reason why we offer such high-level support and standard of service because we never take on more than we can handle.</p>
  <p>As soon as we reach close to our signup limit, we’ll no longer be able to onboard until we’ve scaled up operations further - this could take a month or two.</p>
  <p>Since I started Bright Warrow Dispatch, I’ve had to close our doors to new sign-ups no less than on 4 separate occasions.</p>
</div>
<a class="btn" href="#" style="left:203px;top:3876px;width:127px;height:30px">Learn More</a>
<div class="art" role="img" aria-label="Interior store screenshot with sunglasses bubble shipping from the United States" style="left:629px;top:3612px;width:363px;height:300px;background:linear-gradient(135deg,#f7f7f8,#ece8e4 55%,#e4e4ea)"></div>

<!-- CTA band -->
<svg class="abs" style="left:0;top:3925px" width="1200" height="285" viewBox="0 0 1200 285" aria-hidden="true">
  <path d="M0 60 C150 20 260 10 420 40 C620 80 760 90 920 40 C1040 5 1130 10 1200 20 L1200 285 L0 285 Z" fill="#e8191f"/>
</svg>
<div class="abs" role="img" aria-label="Leather boot in a circle" style="left:229px;top:3947px;width:115px;height:106px;border-radius:50%;background:linear-gradient(135deg,#e8e8e8,#5a5f57)"></div>
<div class="abs" role="img" aria-label="Wristwatch in a circle" style="left:855px;top:3982px;width:96px;height:88px;border-radius:50%;background:linear-gradient(135deg,#3a3a3a,#c02a2a)"></div>
<h2 class="sec-title" style="top:4060px;color:var(--white);font-size:28px">Start your dropshipping business today</h2>
<a class="btn" href="#" style="left:536px;top:4121px;width:127px;height:28px;background:var(--white);color:var(--red)">Start your Free trial</a>
<div class="abs" role="img" aria-label="Smartphone showing a store app in a circle" style="left:176px;top:4141px;width:106px;height:114px;border-radius:50%;border:4px solid #fff;background:linear-gradient(135deg,#f3f3f3,#c9c9d0)"></div>
<div class="abs" role="img" aria-label="Blue umbrella in a circle" style="left:869px;top:4144px;width:106px;height:111px;border-radius:50%;border:4px solid #fff;background:linear-gradient(135deg,#dfe9fb,#2f6fd8)"></div>

<!-- Footer -->
<div class="logo" style="left:203px;top:4300px;font-size:26px">LOGO</div>
<p class="abs" style="left:203px;top:4345px;width:165px;font-size:11px;line-height:1.65">He could have transformed this campaign and product into a long-term, consistently performing brand, without the worry of scaling back or pausing during the Chinese holiday occasions.</p>
<div class="foot-col" style="left:446px"><h5>Company</h5><a href="#">Contact Us</a><a href="#">Privacy Policy</a><a href="#">Terms of use</a><a href="#">Cookie Policy</a><a href="#">Disclaimer</a></div>
<div class="foot-col" style="left:670px"><h5>Integrations</h5><a href="#">Shopwell</a><a href="#">Sitecraft</a><a href="#">StoreForge</a><a href="#">Leapcart</a></div>
<div class="foot-col" style="left:902px"><h5>Resources</h5><a href="#">Help Center</a><a href="#">Affiliate Program</a><a href="#">Become a supplier</a><a href="#">Our Blog</a><a href="#">Supplier list</a></div>
<div class="abs" style="left:0;top:4490px;width:1200px;height:1px;background:var(--line)"></div>
<p class="abs" style="left:0;top:4506px;width:1200px;text-align:center;font-size:11px">Copyright © 2010-2023 e-Commerce store owners and dropshippers</p>

</div>
</body>
</html>
```